NZ First of it's kind solutions directory and marketplace for busy Mums needs a business card design

We need a business card design for our new nationwide business in NZ (long term plans to go global). We provide solutions to the everyday challenges that busy Mums face by connecting them with quality communities and suppliers of carefully selected, relevant products and services. We sell direct via our online marketplace. The final design should communicate our values of inclusivity, quality and smart solutions. Colours should incorporate our logo colour palette of #477077 and #6ba8b2. Our website is at https://www.brightnestly.com

Target Market(s)

busy Mums, Age 28 – 50, female, income over $100K, location main centres NZ primarily but NZ wide. Is likely juggling work or career with a young family. Probably had hobbies which have fallen by the wayside.
-Wants to succeed in her chosen career without compromising on family life
-to successfully juggle her career without feeling like she is compromising her children
- Is time poor, something always has to give and it’s generally her health (she’ll stay up late, get stressed)
- probably ex corporate or professional career. Has discretional income

Industry/Entity Type

Business

Contact Information for Business Card

Lena Hartwell, Founder, BrightNestly.com (Strapline Find; Match; Sorted), 48 Kowhai Terrace, Ferndale, Auckland 1071, New Zealand. Mob: 021 437 518 Ph: +64 (0)9 581 4706

Font styles to use
Other font styles liked:
• Raleway, and/or Architects Daughter

Colors
00a990
33b8a4
86cfc6
cfeae6

Requirements
Must have
• the above details, streamline. the logo and colours associated with those logos
Should not have
• foil or metallic colours

```html
<!DOCTYPE html>
<html lang="en">
<head>
<meta charset="utf-8">
<title>BrightNestly — Business Card</title>
<link rel="stylesheet" href="https://fonts.googleapis.com/css2?family=Roboto:wght@400;500;700&family=Roboto+Condensed:wght@700&display=swap">
<style>
  :root {
    --teal-dark: #477077;
    --teal-light: #6ba8b2;
    --paper: #f3f3f3;
    --ink: #4d4d4d;
    --rule: #c9c9c9;
    --backdrop: #2b2b2b;
    --white: #ffffff;
  }
  * { margin: 0; padding: 0; box-sizing: border-box; }
  html, body {
    width: 1200px; height: 960px; overflow: hidden;
    background: var(--backdrop);
    font-family: "Roboto", Arial, sans-serif;
  }
  .canvas { position: relative; width: 1200px; height: 960px; }

  .card {
    position: absolute; width: 600px; height: 343px;
    border-radius: 18px; overflow: hidden;
  }
  .card--front { left: 314px; top: 113px; background: var(--paper); }
  .card--back  { left: 311px; top: 472px; background: var(--teal-light); }

  .front-band { position: absolute; left: 0; bottom: 0; width: 600px; height: 12px; }

  .brand {
    position: absolute; display: flex; align-items: center; gap: 12px;
    font-family: "Roboto", Arial, sans-serif; font-weight: 500; white-space: nowrap;
  }
  .brand__dot { width: 22px; height: 22px; border-radius: 50%; flex: none; }
  .brand--front { left: 54px; top: 150px; font-size: 34px; color: var(--teal-dark); }
  .brand--front .brand__dot { background: var(--teal-dark); }
  .brand--back { left: 130px; top: 138px; font-size: 50px; color: var(--white); }
  .brand--back .brand__dot { background: var(--teal-dark); width: 32px; height: 32px; }

  .divider {
    position: absolute; left: 321px; top: 99px; width: 1px; height: 148px;
    background: var(--rule);
  }

  .contact { position: absolute; left: 348px; top: 93px; color: var(--ink); }
  .contact__name {
    font-family: "Roboto Condensed", "Arial Narrow", sans-serif; font-weight: 700;
    font-size: 21px; color: var(--teal-dark); letter-spacing: 0.2px; line-height: 24px;
  }
  .contact__role { font-size: 15px; font-weight: 500; color: var(--teal-light); line-height: 18px; }
  .contact__address { margin-top: 8px; font-size: 15px; line-height: 19px; }
  .contact__lines { margin-top: 7px; list-style: none; font-size: 15px; line-height: 19.5px; }
  .contact__lines li { display: flex; align-items: center; gap: 8px; }
  .contact__lines svg { width: 14px; height: 14px; flex: none; fill: var(--teal-dark); }

  .strapline {
    position: absolute; left: 0; width: 600px; top: 285px; text-align: center;
    font-size: 15px; color: var(--white);
  }
</style>
</head>
<body>
<main class="canvas">
  <section class="card card--front" aria-label="Business card front">
    <div class="brand brand--front"><span class="brand__dot"></span>BrightNestly</div>
    <div class="divider"></div>
    <div class="contact">
      <p class="contact__name">LENA HARTWELL</p>
      <p class="contact__role">FOUNDER</p>
      <p class="contact__address">48 Kowhai Terrace, Ferndale<br>Auckland 1071, New Zealand.</p>
      <ul class="contact__lines">
        <li><svg viewBox="0 0 24 24" aria-hidden="true"><path d="M6.6 10.8a15.1 15.1 0 0 0 6.6 6.6l2.2-2.2a1 1 0 0 1 1-.25 11.4 11.4 0 0 0 3.6.57 1 1 0 0 1 1 1V20a1 1 0 0 1-1 1A17 17 0 0 1 3 4a1 1 0 0 1 1-1h3.5a1 1 0 0 1 1 1c0 1.25.2 2.45.57 3.57a1 1 0 0 1-.25 1z"/></svg>+64 (0)9 581 4706</li>
        <li><svg viewBox="0 0 24 24" aria-hidden="true"><path d="M7 1h10a2 2 0 0 1 2 2v18a2 2 0 0 1-2 2H7a2 2 0 0 1-2-2V3a2 2 0 0 1 2-2zm0 3v14h10V4zm5 15.5a1.2 1.2 0 1 0 0 2.4 1.2 1.2 0 0 0 0-2.4z"/></svg>021 437 518</li>
        <li><svg viewBox="0 0 24 24" aria-hidden="true"><circle cx="12" cy="12" r="10"/><path d="M7 7c2 0 3 1 3 3s2 1 2 3-2 2-2 4l-2 2M15 4c0 2 1 3 3 3M17 13c-1 0-2 1-2 3s1 2 2 2" stroke="#f3f3f3" stroke-width="1.6" fill="none"/></svg>BrightNestly.com</li>
      </ul>
    </div>
    <svg class="front-band" viewBox="0 0 600 12" aria-hidden="true">
      <polygon points="0,0 393,0 389,12 0,12" fill="var(--teal-dark)"/>
      <polygon points="393,0 397,0 393,12 389,12" fill="var(--white)"/>
      <polygon points="397,0 600,0 600,12 393,12" fill="var(--teal-light)"/>
    </svg>
  </section>

  <section class="card card--back" aria-label="Business card back">
    <div class="brand brand--back"><span class="brand__dot"></span>BrightNestly</div>
    <p class="strapline">Find; Match; Sorted</p>
  </section>
</main>
</body>
</html>
```